Boutique Barre Studio in Geneva

Business card for pilates and dance studio. We are a brand new studio and love our fresh image with our yellow color. This business card is meant for our founder.

```html
<!DOCTYPE html>
<html lang="en">
<head>
<meta charset="utf-8">
<title>plieform studio – Business Card</title>
<link href="https://fonts.googleapis.com/css2?family=Arimo:ital,wght@0,400;0,700;1,400&display=swap" rel="stylesheet">
<style>
  :root {
    --page: #e9e9e6;
    --card: #262626;
    --yellow: #f2e985;
    --white: #f4f4f4;
    --shadow: rgba(0, 0, 0, 0.25);
  }
  * { margin: 0; padding: 0; box-sizing: border-box; }
  html, body {
    width: 1200px;
    height: 900px;
    overflow: hidden;
    background: var(--page);
    font-family: "Arimo", Arial, sans-serif;
  }
  .sheet {
    position: relative;
    width: 1200px;
    height: 900px;
  }
  .card {
    position: absolute;
    left: 280px;
    width: 640px;
    height: 366px;
    background: var(--card);
    border-radius: 20px;
    overflow: hidden;
    box-shadow: 0 10px 30px var(--shadow);
  }
  .card--front { top: 60px; }
  .card--back { top: 474px; }

  .card__edge {
    position: absolute;
    left: 0; right: 0; bottom: 0;
    height: 12px;
    background: var(--yellow);
  }

  .brand {
    position: absolute;
    color: var(--yellow);
    font-weight: 400;
    letter-spacing: 0.02em;
    white-space: nowrap;
  }
  .card--front .brand {
    top: 62px;
    left: 0; right: 0;
    text-align: center;
    font-size: 56px;
  }
  .card--back .brand {
    top: 0; bottom: 0; left: 0; right: 0;
    display: flex;
    align-items: center;
    justify-content: center;
    font-size: 64px;
  }

  .person {
    position: absolute;
    left: 40px;
    top: 198px;
    width: 238px;
    text-align: right;
  }
  .person__name {
    color: var(--yellow);
    font-weight: 700;
    font-size: 22px;
    letter-spacing: 0.03em;
    text-transform: uppercase;
  }
  .person__role {
    color: var(--white);
    font-style: italic;
    font-size: 14px;
    margin-top: 4px;
  }

  .divider {
    position: absolute;
    left: 300px;
    top: 196px;
    width: 1px;
    height: 62px;
    background: var(--yellow);
  }

  .contacts {
    position: absolute;
    left: 322px;
    top: 194px;
    list-style: none;
  }
  .contacts__item {
    display: flex;
    align-items: center;
    gap: 8px;
    color: var(--white);
    font-style: italic;
    font-size: 14px;
    line-height: 22px;
  }
  .contacts__icon {
    width: 13px;
    height: 13px;
    flex: none;
  }

  .address {
    position: absolute;
    left: 0; right: 0;
    top: 296px;
    text-align: center;
    color: var(--white);
    font-style: italic;
    font-size: 14px;
  }
</style>
</head>
<body>
<main class="sheet">

  <section class="card card--front" aria-label="Business card front">
    <div class="brand">plieform studio</div>

    <div class="person">
      <p class="person__name">Camille Duret</p>
      <p class="person__role">CEO/Founder</p>
    </div>

    <div class="divider"></div>

    <ul class="contacts">
      <li class="contacts__item">
        <svg class="contacts__icon" viewBox="0 0 16 16" aria-hidden="true">
          <path fill="#f2e985" d="M3.6 1.2l2.3 2.6-1.3 1.7c.8 2 2.2 3.4 4.2 4.2l1.7-1.3 2.6 2.3-1.2 2.6C6.5 13.3 2.7 9.5 1 3.1z"/>
        </svg>
        022-555-0148
      </li>
      <li class="contacts__item">
        <svg class="contacts__icon" viewBox="0 0 16 16" aria-hidden="true">
          <rect x="1" y="3" width="14" height="10" fill="#f2e985"/>
          <path d="M1 3l7 6 7-6" fill="none" stroke="#262626" stroke-width="1.4"/>
        </svg>
        hello@plieformstudio.ch
      </li>
      <li class="contacts__item">
        <svg class="contacts__icon" viewBox="0 0 16 16" aria-hidden="true">
          <circle cx="8" cy="8" r="6.5" fill="none" stroke="#f2e985" stroke-width="1.5"/>
          <ellipse cx="8" cy="8" rx="2.6" ry="6.5" fill="none" stroke="#f2e985" stroke-width="1.2"/>
          <path d="M1.5 8h13" stroke="#f2e985" stroke-width="1.2"/>
        </svg>
        www.plieformstudio.ch
      </li>
    </ul>

    <p class="address">14 Rue du Rhône, 1204 Geneva, Switzerland</p>

    <div class="card__edge"></div>
  </section>

  <section class="card card--back" aria-label="Business card back">
    <div class="brand">plieform studio</div>
  </section>

</main>
</body>
</html>
```